SIGN UP PAGE AND CHECK OUT PROCESS DESIGN NEEDED

I offer a subscription service. Two products that offer the same exact features just two different prices as the cheaper product offers limited of all the features....<br/><br/>PLEASE USE EXISTING THEME OF CURRENT DESIGN JUST MAKE AN IMPROVED SIGN UP PAGE. <br/><br/><br/>NEED SIGN UP PAGE for a subscription service..... <br/>This is my current sign up page, only offers one product: https://www.brightpromoperks.example/?page=signup <br/><br/>Please use all the same fields and content listed on this sign up page also please do a fake sign up to see the credit card page. I also need the credit card page to be designed....or if you want to combine the sign up and credit card page, etc. all in one I am open for that too....my goal is a super quick an easy sign up for customer. <br/><br/> AL A CARTE PROGRAM<br/>1 CERTIFICATE TYPE EACH MONTH<br/>$49/MTH MONTH TO MONTH BASIS NO CONTRACTS<br/>$239 ONE TIME PAYMENT FOR 6 MTHS OF SERVICE<br/>$399 ONE TIME PAYMENT FOR 12 MONTHS OF SERVICE<br/><br/>FEATURES:<br/><br/>UNLIMITED CERTIFICATE PDF DOWNLOADS<br/><br/>UNLIMITED E-MAIL CERTIFICATES<br/><br/>UNLIMITED TEXT/SMS CERTIFICATES<br/><br/>UNLIMITED API USAGE<br/><br/>UNLIMITED WEB BANNER CERTIFICATES<br/><br/>FULL REDEMPTION TRACKING<br/><br/>CERTIFICATE DISTRIBUTION REPORTS<br/><br/>WHITE LABEL REDEMPTION SITE<br/><br/>END USER MARKETING VIDEOS<br/><br/>MARKETING POSTERS AND FLYERS<br/><br/>PRODUCT DESCRIPTIONI BROCHURES<br/><br/>THE LATEST TIPS<br/><br/>SEPERATE REDEMPTION WEBSITES<br/><br/>CONTACT US 24/7<br/><br/>AFFILIATE PROGRAM<br/><br/>DISCOUNT TRAVEL BOOKING ENGINE<br/><br/>UNLIMITED PROGRAM<br/>UNLIMITED AMOUNTS OF ALL THE CERTIFICATES<br/>$99/MTH MONTH TO MONTH BASIS NO CONTRACTS<br/>$495 ONE TIME PAYMENT FOR 6 MTHS OF SERVICE<br/>$2,295 ONE TIME PAYMENT FOR 12 MONTHS OF SERVICE<br/><br/>FEATURES:<br/><br/>UNLIMITED CERTIFICATE PDF DOWNLOADS<br/><br/>UNLIMITED E-MAIL CERTIFICATES<br/><br/>UNLIMITED TEXT/SMS CERTIFICATES<br/><br/>UNLIMITED API USAGE<br/><br/>UNLIMITED WEB BANNER CERTIFICATES<br/><br/>FULL REDEMPTION TRACKING<br/><br/>CERTIFICATE DISTRIBUTION REPORTS<br/><br/>WHITE LABEL REDEMPTION SITE<br/><br/>END USER MARKETING VIDEOS<br/><br/>MARKETING POSTERS AND FLYERS<br/><br/>PRODUCT DESCRIPTIONI BROCHURES<br/><br/>THE LATEST TIPS<br/><br/>SEPERATE REDEMPTION WEBSITES<br/><br/>CONTACT US 24/7<br/><br/>AFFILIATE PROGRAM<br/><br/>DISCOUNT TRAVEL BOOKING ENGINE<br/><br/><br/>

Target Market(s)

B2B SMALL BUSINESS OWNERS
MARKETERS
ADVERTISERS

Industry/Entity Type

Digital Marketing

Number of Pages Required

3 page

Colors

Designer to choose colors to be used in the design.

Requirements
Must have
• MUST MATCH EXISTING THEME
Nice to have
• A VERY MODERN DESIGN

```html
<!DOCTYPE html>
<html lang="en">
<head>
<meta charset="utf-8">
<title>Sign Up – Bright Promo Perks</title>
<link href="https://fonts.googleapis.com/css2?family=Lato:wght@300;400;700;900&display=swap" rel="stylesheet">
<style>
:root{
  --ink:#2b2f36;
  --muted:#5c6470;
  --dark:#1b1c1f;
  --darker:#111214;
  --blue:#1676c9;
  --blue-bright:#1d86dc;
  --navy:#0f1e30;
  --orange:#f57f17;
  --green:#5cc46a;
  --line:#e3e6ea;
  --soft:#f4f5f7;
  --pink:#f8ecea;
  --white:#ffffff;
}
*{box-sizing:border-box;margin:0;padding:0}
html,body{width:1200px;height:3482px;overflow:hidden}
body{font-family:"Lato",Arial,sans-serif;color:var(--ink);background:var(--white);position:relative}
a{color:inherit;text-decoration:none}

/* header */
.site-header{height:135px;background:var(--dark);position:relative}
.account-tabs{position:absolute;right:22px;top:0;display:flex;height:36px}
.account-tabs span{display:flex;align-items:center;gap:8px;color:var(--white);font-size:15px;font-weight:700;padding:0 26px}
.account-tabs .login{background:#3a3c41;border-radius:0 0 0 18px}
.account-tabs .signup{background:var(--blue);border-radius:0 0 18px 0}
.brand{position:absolute;left:70px;top:44px;display:flex;align-items:center;gap:12px}
.brand-mark{width:46px;height:46px;background:var(--blue-bright);border-radius:6px}
.brand-name{font-size:34px;font-weight:700;color:var(--blue-bright);letter-spacing:1px}
.contact-strip{position:absolute;right:22px;top:62px;display:flex;align-items:center;gap:22px;color:var(--white)}
.contact-strip .phone-dot{width:40px;height:40px;border-radius:50%;background:var(--blue);display:flex;align-items:center;justify-content:center}
.contact-strip p{font-size:18px;line-height:25px}
.contact-strip b{font-weight:700}

.main-nav{height:46px;background:var(--blue);display:flex;align-items:center;padding-left:111px}
.main-nav a{color:var(--white);font-size:14px;font-weight:400;letter-spacing:.4px;margin-right:64px}

.page-hero{height:139px;background:linear-gradient(100deg,#b9b2d6 0%,#d6c4d8 45%,#e9c7c6 75%,#c9b3cf 100%);display:flex;align-items:center;justify-content:center}
.page-hero h1{color:var(--white);font-weight:300;font-size:40px;letter-spacing:1px}

/* pricing */
.pricing{position:absolute;top:370px;left:70px;width:1060px;height:910px}
.col{position:absolute;top:0}
.col-features{left:0;width:338px;border:1px solid var(--line)}
.col-plan{width:338px}
.col-alacarte{left:376px}
.col-unlimited{left:722px}
.col-head{height:85px;display:flex;flex-direction:column;align-items:center;justify-content:center;color:var(--white);position:relative;overflow:hidden}
.col-features .col-head{background:#4b4e55;font-size:20px;font-weight:900;letter-spacing:1px}
.col-alacarte .col-head{background:var(--blue)}
.col-unlimited .col-head{background:var(--navy)}
.col-head h2{font-size:21px;font-weight:900}
.col-head p{font-size:15px;margin-top:2px}
.ribbon{position:absolute;left:-26px;top:10px;width:100px;height:16px;background:var(--orange);transform:rotate(-45deg)}
.costing{height:86px;display:flex;align-items:center;justify-content:space-around;background:var(--soft)}
.col-features .costing{justify-content:center;font-size:15px;font-weight:700}
.price{text-align:center;color:#6ea4d8}
.price strong{display:block;font-size:26px;font-weight:400}
.price small{font-size:12px}
.row{height:42.8px;border-top:1px solid var(--line);display:flex;align-items:center;justify-content:center;font-size:13px;color:#3a3f47}
.col-plan .row{background:#f8f9fa;border-top:1px solid #eceef1}
.col-plan .rows{border-bottom:1px solid #eceef1}
.select-btn{margin-top:8px;height:45px;background:var(--orange);color:var(--white);font-weight:900;font-size:17px;display:flex;align-items:center;justify-content:center;letter-spacing:.5px}

/* accordion */
.accordion-bar{position:absolute;left:70px;width:1060px;height:54px;background:var(--blue);color:var(--white);display:flex;align-items:center;justify-content:space-between;padding:0 38px;font-size:21px;font-weight:700}
.bar-about{top:1323px}
.bar-payment{top:1388px}
.accordion-bar span.sign{font-size:32px;font-weight:300}

.payment-panel{position:absolute;left:70px;top:1442px;width:1060px;height:1285px;background:#f7f7f8}
.intro{position:absolute;left:37px;top:18px;font-size:14px;color:var(--muted)}
.intro small{display:block;font-size:12px;margin-top:4px}
.summary{position:absolute;left:37px;top:81px;width:986px;height:300px;background:var(--pink);border:1px solid #eed9d4;padding:28px 36px;font-size:14px;color:#333}
.summary h3{font-size:19px;font-weight:400}
.summary .street{margin-top:4px}
.summary dl{margin-top:28px;line-height:23px}
.summary dt{font-weight:700;display:inline}
.totals{position:absolute;left:36px;right:36px;top:208px;line-height:22px;font-weight:700}
.totals div{display:flex;justify-content:space-between}
.totals span:last-child{font-weight:400;width:110px}

.card-info{position:absolute;left:37px;top:420px;width:986px}
.card-info h4{font-size:14px;font-weight:700;letter-spacing:.5px}
.field{position:absolute;border-bottom:1px solid #c9cdd3;height:34px;font-size:13px;color:var(--muted);padding-top:10px}
.cvv-note{position:absolute;top:172px;left:0;width:986px;font-size:12.5px;line-height:18px;color:#444}
.agree{position:absolute;top:235px;left:0;font-size:13px;display:flex;align-items:center;gap:10px}
.agree i{width:13px;height:13px;border:1px solid #777;background:var(--white);display:inline-block}
.signup-btn{position:absolute;top:306px;left:0;width:218px;height:44px;background:var(--navy);color:var(--white);font-weight:900;font-size:15px;display:flex;align-items:center;justify-content:center;letter-spacing:.5px}

.terms{position:absolute;left:37px;top:816px;width:986px;height:440px;border:2px solid #d0d3d8;background:var(--white);padding:24px 28px;font-size:11.6px;line-height:16.5px;color:#333}
.terms h5{font-size:16px;font-weight:400;margin-bottom:14px}
.terms h6{font-size:12px;font-weight:700;margin-top:10px}

/* footer */
.site-footer{position:absolute;left:0;top:2850px;width:1200px;height:585px;background:var(--dark);color:#d7d9dc}
.footer-col h3{font-size:19px;font-weight:400;color:var(--white);margin-bottom:18px}
.quick-links{position:absolute;left:70px;top:45px}
.quick-links li{list-style:none;font-size:14.5px;line-height:29.6px}
.quick-links li::before{content:"›";margin-right:10px}
.contact-details{position:absolute;left:432px;top:45px;font-size:12.5px;line-height:18px}
.contact-details .item{display:flex;gap:10px;margin-top:6px}
.contact-details b{font-size:13px}
.hours{margin-top:56px}
.footer-brand{position:absolute;left:889px;top:48px}
.footer-brand .name{font-size:22px;font-weight:700;color:var(--blue-bright)}
.socials{display:flex;gap:12px;margin-top:26px;margin-left:45px}
.socials i{width:30px;height:30px;border-radius:50%;display:block}
.copyright{position:absolute;left:0;top:3435px;width:1200px;height:47px;background:var(--darker);color:#d7d9dc;font-size:14px;display:flex;align-items:center;justify-content:center}
</style>
</head>
<body>
<svg width="0" height="0" style="position:absolute">
  <defs>
    <symbol id="tick" viewBox="0 0 20 20">
      <circle cx="10" cy="10" r="8.5" fill="none" stroke="#5cc46a" stroke-width="1.6"/>
      <path d="M6 10.3l2.8 2.8L14.3 7.5" fill="none" stroke="#5cc46a" stroke-width="1.8" stroke-linecap="round" stroke-linejoin="round"/>
    </symbol>
  </defs>
</svg>

<header class="site-header">
  <div class="account-tabs">
    <span class="login">
      <svg width="14" height="14" viewBox="0 0 14 14"><path d="M1 7h8M6 4l3 3-3 3M9 1h4v12H9" fill="none" stroke="#fff" stroke-width="1.6"/></svg>LOGIN</span>
    <span class="signup">
      <svg width="16" height="14" viewBox="0 0 16 14"><circle cx="6" cy="4" r="3" fill="#fff"/><path d="M0 13c0-4 3-5 6-5s6 1 6 5z" fill="#fff"/><path d="M13 3v5M10.5 5.5h5" stroke="#fff" stroke-width="1.5"/></svg>SIGN UP</span>
  </div>
  <div class="brand"><span class="brand-mark"></span><span class="brand-name">BRIGHT PROMO PERKS</span></div>
  <div class="contact-strip">
    <span class="phone-dot"><svg width="18" height="18" viewBox="0 0 24 24"><path d="M6.6 10.8a15 15 0 006.6 6.6l2.2-2.2c.3-.3.7-.4 1-.2 1.1.4 2.3.6 3.6.6.6 0 1 .4 1 1V20c0 .6-.4 1-1 1A17 17 0 013 4c0-.6.4-1 1-1h3.5c.6 0 1 .4 1 1 0 1.3.2 2.5.6 3.6.1.3 0 .7-.2 1z" fill="#fff"/></svg></span>
    <p>USA Office : <b>555-014-2230</b><br>International : <b>1-800-555-0147</b></p>
  </div>
</header>

<nav class="main-nav">
  <a href="#">HOME</a><a href="#">OUR INCENTIVES</a><a href="#">SAMPLES</a><a href="#">AFFILIATES</a><a href="#">TESTIMONIALS</a><a href="#">FAQ</a><a href="#">CONTACT</a>
</nav>

<section class="page-hero" role="img" aria-label="Soft pastel banner background"><h1>SIGN UP</h1></section>

<section class="pricing">
  <div class="col col-features">
    <div class="col-head">FEATURES</div>
    <div class="costing">Costing</div>
    <div class="rows">
      <div class="row">Unlimited certificate pdf downloads</div>
      <div class="row">Unlimited e-mail certificates</div>
      <div class="row">Unlimited text/sms certificates</div>
      <div class="row">Unlimited api usage</div>
      <div class="row">Unlimited web banner certificates</div>
      <div class="row">Full redemption tracking</div>
      <div class="row">Certificate distribution reports</div>
      <div class="row">White label redemption site</div>
      <div class="row">End user marketing videos</div>
      <div class="row">Marketing posters and flyers</div>
      <div class="row">Product description brochures</div>
      <div class="row">The latest tips</div>
      <div class="row">Seperate redemption websites</div>
      <div class="row">Contact us 24/7</div>
      <div class="row">Affiliate program</div>
      <div class="row">Discount travel booking engine</div>
    </div>
  </div>

  <div class="col col-plan col-alacarte">
    <div class="col-head"><h2>AL A CARTE PROGRAM</h2><p>1 Certificate Type Each Month</p></div>
    <div class="costing">
      <div class="price"><strong>$49</strong><small>per month</small></div>
      <div class="price"><strong>$239</strong><small>for 6 months</small></div>
      <div class="price"><strong>$399</strong><small>for 12 months</small></div>
    </div>
    <div class="rows">
      <div class="row"><svg width="20" height="20"><use href="#tick"/></svg></div>
      <div class="row"><svg width="20" height="20"><use href="#tick"/></svg></div>
      <div class="row"><svg width="20" height="20"><use href="#tick"/></svg></div>
      <div class="row"><svg width="20" height="20"><use href="#tick"/></svg></div>
      <div class="row"><svg width="20" height="20"><use href="#tick"/></svg></div>
      <div class="row"><svg width="20" height="20"><use href="#tick"/></svg></div>
      <div class="row"><svg width="20" height="20"><use href="#tick"/></svg></div>
      <div class="row"><svg width="20" height="20"><use href="#tick"/></svg></div>
      <div class="row"><svg width="20" height="20"><use href="#tick"/></svg></div>
      <div class="row"><svg width="20" height="20"><use href="#tick"/></svg></div>
      <div class="row"><svg width="20" height="20"><use href="#tick"/></svg></div>
      <div class="row"><svg width="20" height="20"><use href="#tick"/></svg></div>
      <div class="row"><svg width="20" height="20"><use href="#tick"/></svg></div>
      <div class="row"><svg width="20" height="20"><use href="#tick"/></svg></div>
      <div class="row"><svg width="20" height="20"><use href="#tick"/></svg></div>
      <div class="row"><svg width="20" height="20"><use href="#tick"/></svg></div>
    </div>
    <a class="select-btn" href="#">SELECT</a>
  </div>

  <div class="col col-plan col-unlimited">
    <div class="col-head"><span class="ribbon"></span><h2>UNLIMITED PROGRAM</h2><p>Unlimited Amounts Of All The Certificates</p></div>
    <div class="costing">
      <div class="price"><strong>$99</strong><small>per month</small></div>
      <div class="price"><strong>$495</strong><small>for 6 months</small></div>
      <div class="price"><strong>$2,295</strong><small>for 12 months</small></div>
    </div>
    <div class="rows">
      <div class="row"><svg width="20" height="20"><use href="#tick"/></svg></div>
      <div class="row"><svg width="20" height="20"><use href="#tick"/></svg></div>
      <div class="row"><svg width="20" height="20"><use href="#tick"/></svg></div>
      <div class="row"><svg width="20" height="20"><use href="#tick"/></svg></div>
      <div class="row"><svg width="20" height="20"><use href="#tick"/></svg></div>
      <div class="row"><svg width="20" height="20"><use href="#tick"/></svg></div>
      <div class="row"><svg width="20" height="20"><use href="#tick"/></svg></div>
      <div class="row"><svg width="20" height="20"><use href="#tick"/></svg></div>
      <div class="row"><svg width="20" height="20"><use href="#tick"/></svg></div>
      <div class="row"><svg width="20" height="20"><use href="#tick"/></svg></div>
      <div class="row"><svg width="20" height="20"><use href="#tick"/></svg></div>
      <div class="row"><svg width="20" height="20"><use href="#tick"/></svg></div>
      <div class="row"><svg width="20" height="20"><use href="#tick"/></svg></div>
      <div class="row"><svg width="20" height="20"><use href="#tick"/></svg></div>
      <div class="row"><svg width="20" height="20"><use href="#tick"/></svg></div>
      <div class="row"><svg width="20" height="20"><use href="#tick"/></svg></div>
    </div>
    <a class="select-btn" href="#">SELECT</a>
  </div>
</section>

<div class="accordion-bar bar-about"><span>About Yourself</span><span class="sign">+</span></div>
<div class="accordion-bar bar-payment"><span>Payment Information</span><span class="sign">−</span></div>

<section class="payment-panel">
  <p class="intro">Please verify your order and enter your credit card info below<small>**The information you provide below must match the billing details of where your billing statement is mailed to from your bank.</small></p>

  <div class="summary">
    <h3>Dana Whitlow</h3>
    <p class="street">4410 Sample Street</p>
    <dl>
      <div><dt>Address:</dt> Lakeview, CA 90000, US</div>
      <div><dt>Phone No:</dt> 5550142288</div>
      <div><dt>E-mail:</dt> dana@samplemail.example</div>
      <div><dt>Username:</dt> danawhitlow</div>
    </dl>
    <div class="totals">
      <div><span>One Time Set Up Fee:</span><span>$99.00</span></div>
      <div><span>Monthly Fee:</span><span>$99.00/Month</span></div>
      <div><span>Total Charged Today:</span><span>$198.00</span></div>
    </div>
  </div>

  <div class="card-info">
    <h4>CARD INFORMATION</h4>
    <div class="field" style="top:42px;left:0;width:404px">Credit Card Type*</div>
    <div class="field" style="top:42px;left:534px;width:452px">Credit Card No.*</div>
    <div class="field" style="top:110px;left:0;width:275px">Credit Card Exp Month*</div>
    <div class="field" style="top:110px;left:357px;width:275px">Credit Card Exp Year</div>
    <div class="field" style="top:110px;left:711px;width:275px">Credit Card CVV2</div>
    <p class="cvv-note">The CVV2 is the three digit code on the signature panel on the back of most cards, after the card number. On some cards it is instead the four digit code printed above the credit card number on the front of the card.</p>
    <label class="agree"><i></i>I Agree to the Payments Terms and Conditions stated below</label>
    <a class="signup-btn" href="#">SIGN UP NOW</a>
  </div>

  <div class="terms">
    <h5>Payment Terms and Conditions</h5>
    <h6>$99 Recurring Billing</h6>
    <p>You must provide a valid billing method. BPPG will immediately charge your account $198. BPPG will continue to debit your account automatically every month for $99. This process will remain in full force until BPPG receives a cancellation notice through the online support ticket system, conveniently located in your password-protected control panel area. We must receive the cancellation notice a minimum of 3 business days (not counting holidays or weekends) prior to your next billing date in order to avoid being billed for the following month. Business days are Monday through Friday only and do not include holidays or weekends.</p>
    <h6>Refund Policy</h6>
    <p>We provide a 3-day refund policy. We will refund you 100%, provided that you request your refund within 3 days of your initial enrollment date. We pay our vendors after 3-days for every member. Therefore, we cannot honor or authorize refund requests after 3 days for reimbursement, as we have already forwarded that money to our clients.</p>
    <h6>30 Day Risk-Free Trial Terms &amp; Conditions</h6>
    <p>Our incentive marketing program works, and we are willing to prove that it works at no risk to our new customers.<br>
    Our incentives work but there is participation required by our customers; you must run incentive marketing campaigns within your business to receive your desired results.<br>
    Therefore to participate and to receive the refund you must use our service in the first 30 days from your membership sign up date. To qualify for the 30 day risk free trial refund you need to have at least one (1) paid redemption in the first 30 days of your membership. Redeeming a 'Free Wellness Savings Card' does not satisfy your requirement because it is not a paid redemption.<br>
    If you are not completely satisfied with the redemption and or the fulfillment process within the first 30 days we will refund 100% of your membership fees per your request.<br>
    By signing up with our company you understand and acknowledge that in order to qualify you must have at least one (1) paid redemption within the first 30 days of your membership.<br>
    You are also required to cancel within 30 days by submitting a 'Support Ticket' from your 'Main Control Panel' account in order to qualify for the refund. Failure in completing these steps will terminate any members' ability to receive the 30-Day Risk Free Trial refund.</p>
  </div>
</section>

<footer class="site-footer">
  <div class="footer-col quick-links">
    <h3>QUICK LINKS</h3>
    <ul>
      <li>Home</li><li>Our Incentives</li><li>Samples</li><li>Affiliate</li><li>Testimonials</li><li>Faq</li><li>Contact Us</li><li>Terms &amp; Conditions</li><li>Privacy Policy</li><li>Hoteliers</li><li>BPP PDF Flyer</li><li>BPP PDF Brochure</li><li>BPP Certificates List</li><li>How To Use BPP Certificates</li><li>Free Video Ad Mock Up For Marketing</li>
    </ul>
  </div>
  <div class="footer-col contact-details">
    <h3>CONTACT DETAILS</h3>
    <div class="item">
      <svg width="12" height="16" viewBox="0 0 12 16"><path d="M6 0a6 6 0 00-6 6c0 4.5 6 10 6 10s6-5.5 6-10a6 6 0 00-6-6zm0 8.5A2.5 2.5 0 116 3.5a2.5 2.5 0 010 5z" fill="#d7d9dc"/></svg>
      <div><b>Bright Promo Perks Group, Inc.</b><br><br>1200 Harbor View Road<br>Bayside CA 90000</div>
    </div>
    <div class="item hours">
      <svg width="16" height="16" viewBox="0 0 16 16"><rect x="1" y="3" width="14" height="12" rx="1" fill="none" stroke="#d7d9dc" stroke-width="1.4"/><path d="M1 7h14M5 1v4M11 1v4" stroke="#d7d9dc" stroke-width="1.4"/></svg>
      <div>Hours: Mon-Fri 8am - 5pm PST<br>Sat-Sun CLOSED</div>
    </div>
  </div>
  <div class="footer-brand">
    <div class="name">BRIGHT PROMO PERKS</div>
    <div class="socials">
      <i style="background:#3b5ca8"></i><i style="background:#d9322c"></i><i style="background:#1e77b5"></i><i style="background:#1f8fe0"></i>
    </div>
  </div>
</footer>
<div class="copyright">Copyright 2005-2020 Bright Promo Perks Group, Inc. All Rights Reserved.</div>
</body>
</html>
```